We are looking for an effective ad to recruit work from home Loan Officers for our Mortgage Brokerage.
Use the following text...
Earn Mortgage Income in your sleep. Its as easy as 1, 2, 3.....
1) Solicit Potential Applicants (Word of Mouth, Email, Social Media etc.)
2) Take Complete Applications & Submit Them
3) Wait to Get Paid.......(Avg. $2,500 per closing)
"You open the door, we'll finish the deal"
No Experience Necessary
No Goals or Quotas
No Office Hours / Work from Home Office
...and We Fully Reimburse ALL LICENSING FEES!!
Email Resume to mwelby@brightharborloans.example
Bright Harbor Lending Group, Inc.
947 W Caldwell Avenue, #318
Baltimore, MD 21230
NMLS #731860
www.brightharborloans.example
Phone (800) 555-0142
Licensed Mortgage Broker in MD and DC since 1997
Target Market(s)
Professionals looking to earn part time income at Loan Officers, preferably with strong social media following.
Industry/Entity Type
Loan
Look and feel

```html
<!DOCTYPE html>
<html lang="en">
<head>
<meta charset="utf-8">
<title>Bright Harbor Lending Group – Loan Officer Recruitment Flyer</title>
<link rel="stylesheet" href="https://fonts.googleapis.com/css2?family=Montserrat:wght@400;500;600;700;800&family=Nunito+Sans:wght@400;600;700;800&display=swap">
<style>
  :root {
    --backdrop: #5b3c27;
    --paper: #ffffff;
    --paper-shade: #e4e6ea;
    --ink: #111418;
    --navy: #1a4e96;
    --navy-deep: #173f7c;
    --sky: #5cb9ea;
    --sky-light: #7fd0f5;
    --lime: #7cb51f;
    --lime-band: #8dc63f;
    --footer-blue: #1e56a2;
    --phone-blue: #63c6f4;
    --photo-top: #eef2f6;
    --photo-mid: #c9b7a8;
    --photo-low: #7d93b4;
  }
  * { box-sizing: border-box; margin: 0; padding: 0; }
  html, body { width: 1200px; height: 1000px; overflow: hidden; }
  body {
    background: var(--backdrop);
    font-family: "Nunito Sans", Arial, sans-serif;
    position: relative;
  }
  .flyer {
    position: absolute;
    left: 244px; top: 40px;
    width: 713px; height: 922px;
    background: linear-gradient(180deg, var(--paper) 0%, var(--paper) 45%, var(--paper-shade) 100%);
    overflow: hidden;
    box-shadow: 0 6px 18px rgba(0,0,0,.35);
  }
  .hero-photo {
    position: absolute; left: 0; top: 0;
    width: 713px; height: 405px;
    background:
      radial-gradient(ellipse 45% 55% at 58% 48%, var(--photo-mid) 0%, rgba(201,183,168,.5) 55%, rgba(201,183,168,0) 100%),
      linear-gradient(180deg, var(--photo-top) 0%, #dfe5ec 55%, var(--photo-low) 100%);
  }
  .hero-fade {
    position: absolute; left: 0; top: 360px;
    width: 713px; height: 60px;
    background: linear-gradient(180deg, rgba(236,238,241,0) 0%, #eceef1 100%);
  }
  .brand {
    position: absolute; left: 24px; top: 86px;
    display: flex; align-items: center; gap: 10px;
  }
  .brand-dot {
    width: 34px; height: 34px; border-radius: 50%;
    background: var(--navy);
  }
  .brand-name {
    font-family: "Montserrat", Arial, sans-serif;
    font-weight: 700; font-size: 17px; line-height: 1.2;
    color: var(--navy); width: 220px;
  }
  .headline {
    position: absolute; left: 0; top: 403px; width: 713px;
    text-align: center;
    font-family: "Montserrat", Arial, sans-serif;
    font-weight: 700; font-size: 28.5px; color: var(--ink);
    letter-spacing: -0.2px;
  }
  .headline-sub {
    position: absolute; left: 0; top: 434px; width: 713px;
    text-align: center;
    font-family: "Montserrat", Arial, sans-serif;
    font-weight: 700; font-size: 43px; color: var(--navy);
    letter-spacing: 0.5px;
  }
  .steps {
    position: absolute; left: 80px; top: 511px;
    width: 552px; height: 122px;
    background: var(--sky);
    border: 3px solid var(--navy);
    border-radius: 14px;
    display: flex;
    box-shadow: 0 14px 14px -8px rgba(0,0,0,.28);
  }
  .step {
    flex: 1;
    display: flex; flex-direction: column; justify-content: center; align-items: center;
    text-align: center; color: #fff;
    font-size: 17.5px; line-height: 1.28;
    padding: 0 6px;
  }
  .step + .step { border-left: 2px solid var(--sky-light); }
  .step-one { flex: 0 0 230px; }
  .step-two { flex: 0 0 170px; }
  .step strong { color: var(--ink); font-weight: 800; font-size: 17px; }
  .pill {
    position: absolute;
    background: var(--navy);
    color: #fff;
    border-radius: 4px;
    text-align: center;
    font-size: 14.5px; line-height: 22px;
  }
  .pill-tagline { left: 191px; top: 667px; width: 330px; }
  .pill-reimburse { left: 172px; top: 763px; width: 369px; font-size: 15px; }
  .perks {
    position: absolute; left: 62px; top: 697px;
    width: 588px; height: 60px;
    background: #fff;
    border: 2px solid var(--navy);
    border-radius: 8px;
    display: flex; align-items: center; justify-content: space-around;
    padding: 0 10px;
  }
  .perk { display: flex; align-items: center; gap: 4px; }
  .perk-no {
    font-family: "Montserrat", Arial, sans-serif;
    font-weight: 800; font-size: 45px; line-height: 1;
    color: var(--lime); letter-spacing: -1px;
  }
  .perk-text { font-size: 15px; line-height: 1.2; color: var(--ink); }
  .footer-apply {
    position: absolute; left: 0; top: 806px;
    width: 274px; height: 116px;
    background: var(--lime-band);
    padding: 12px 0 0 27px;
    color: var(--ink);
  }
  .apply-label { font-size: 15px; }
  .apply-email { font-size: 14.6px; font-weight: 600; margin-top: 2px; white-space: nowrap; }
  .apply-license { font-size: 14px; line-height: 1.25; margin-top: 12px; }
  .footer-contact {
    position: absolute; left: 274px; top: 806px;
    width: 439px; height: 116px;
    background: var(--footer-blue);
    padding: 10px 0 0 20px;
    color: #fff;
  }
  .contact-phone {
    display: flex; align-items: center; gap: 8px;
    font-family: "Montserrat", Arial, sans-serif;
    font-weight: 700; font-size: 26px; color: var(--phone-blue);
  }
  .contact-company {
    font-family: "Montserrat", Arial, sans-serif;
    font-weight: 500; font-size: 14px; margin-top: 2px; letter-spacing: .2px;
  }
  .contact-address { font-size: 10px; line-height: 1.25; margin-top: 3px; }
  .contact-web { font-size: 12.5px; margin-top: 1px; }
  .social-badge {
    position: absolute; right: 53px; bottom: 14px;
    width: 86px; height: 26px;
    background: #fff; border-radius: 2px;
  }
</style>
</head>
<body>
  <main class="flyer">
    <div class="hero-photo" role="img" aria-label="Photo of a smiling family of four — parents and two children — leaning together in a bright living room"></div>
    <div class="hero-fade"></div>

    <div class="brand">
      <span class="brand-dot"></span>
      <span class="brand-name">Bright Harbor Lending Group, Inc.</span>
    </div>

    <h1 class="headline">Earn Mortgage Income in your sleep.</h1>
    <p class="headline-sub">ITS AS EASY AS 1, 2, 3.....</p>

    <section class="steps">
      <div class="step step-one">Solicit Potential Applicants<strong>(Word of Mouth, Email, Social Media etc.)</strong></div>
      <div class="step step-two">Take Complete Applications &amp; Submit Them</div>
      <div class="step step-three">Wait to Get Paid.......<strong>(Avg. $2,500 per closing)</strong></div>
    </section>

    <p class="pill pill-tagline">"You open the door, we'll finish the deal"</p>

    <section class="perks">
      <div class="perk"><span class="perk-no">NO</span><span class="perk-text">Experience<br>Necessary</span></div>
      <div class="perk"><span class="perk-no">NO</span><span class="perk-text">Goals<br>or Quotas</span></div>
      <div class="perk"><span class="perk-no">NO</span><span class="perk-text">Office Hours / Work<br>from Home Office</span></div>
    </section>

    <p class="pill pill-reimburse">...and We Fully Reimburse ALL LICENSING FEES!!</p>

    <footer>
      <div class="footer-apply">
        <p class="apply-label">Email Resume to</p>
        <p class="apply-email">mwelby@brightharborloans.example</p>
        <p class="apply-license">Licensed Mortgage Broker<br>in MD and DC since 1997</p>
      </div>
      <div class="footer-contact">
        <p class="contact-phone">
          <svg width="22" height="22" viewBox="0 0 22 22" aria-hidden="true">
            <circle cx="11" cy="11" r="10" fill="none" stroke="#ffffff" stroke-width="1.6"/>
            <path d="M7.4 5.6c.5-.4 1.1-.3 1.4.2l1 1.7c.3.5.2 1-.2 1.3l-.7.5c.5 1.3 1.5 2.4 2.8 3l.5-.7c.3-.4.9-.5 1.3-.2l1.7 1c.5.3.6.9.2 1.4l-.8.9c-.6.6-1.5.8-2.3.4-2.7-1.2-4.8-3.3-6-6-.3-.8-.2-1.7.4-2.3z" fill="#ffffff"/>
          </svg>
          (800) 555-0142
        </p>
        <p class="contact-company">BRIGHT HARBOR LENDING GROUP, INC.</p>
        <p class="contact-address">947 W Caldwell Avenue, #318 Baltimore,<br>MD 21230 NMLS #731860</p>
        <p class="contact-web">www.brightharborloans.example</p>
        <div class="social-badge" aria-hidden="true"></div>
      </div>
    </footer>
  </main>
</body>
</html>
```